Fallowmere community hall home page

We are building a modern, responsive website & booking system for our community hall. For this SketchHarbor task, we would like to receive design ideas for the home page.
There are no limits on the colours or fonts that can be used. We are looking for a modern, fresh design with a local/community feel. We don’t have a logo but we also recognise that our name is quite long! … So initials (FCH) instead of the name would be fine.
People book our community hall for a range of activities including: fitness classes, wedding receptions, birthday parties, business meetings, teaching, community events, charity fundraisers and other celebrations.
We have three main goals for the website. The first is that people can check our calendar and make a booking for an available time slot. The second is that they can read about our facilities and the prices for hiring them. The third is that people can find out about upcoming activities & events.
CTA: Book now
A button that links to a booking request form. (The form is not part of this design project)
Primary/Header navigation:
Home | Calendar | Facilities | Prices | Photos | News | Contact
Secondary/Footer navigation:
Chatterbook | Quipper
Login | Register | Privacy policy | Terms & conditions
Example texts (lorem ipsum etc. is also fine):
We have everything you need from a venue, whether it’s an elegant room with ample flexible space, a lavish and elegant hall for a wedding reception, a conference room that fits 125 delegates or a easy access venue to the town centre.
The hall is available for hire for wedding receptions, birthday celebrations, anniversaries, children's parties, presentations, lectures, fitness groups, and will comfortably accommodate all your guests.
This venue is well equipped with a modern kitchen, a range of audio and technical services, hearing loop, licensed bar, conference facilities, disabled access and unlimited free WiFi.
You can use this website to find out more about our rooms, equipment and the services we can offer and use the calendar to see where we have rooms available. You can also book rooms using our online booking system.
To the front of the building is a large public open grassed area across which is a row of shops. To the rear of the building is the large car park, including spaces for blue badge holders and a large enclosed cycle rack. This area also has extensive gardens, with seating and planting areas maintained by local volunteers.
The community hall is run and managed by volunteers of the Fallowmere Community Organisation. Our objectives are to increase opportunities for people living in and around Fallowmere.
We are passionate about being the heart of the community; caring for this community centred property and visitors are at the heart of all we do.
Where to go next
— Check when the hall is free
— Read our booking policy documents
— Make a booking reservation
Amenities
— Free WiFi
— Free car parking
— Fully equipped kitchen
— Hearing loop
Details for our most popular facilities (rooms):
Name: Main hall
Short description: A 127 square metre main hall with entrance lobby, toilets, a well-equipped kitchen and separate storage facilities. Three sets of double doors provide access to a large paved area and the adjacent playing field.
Capacity: 180 people
Price: £10-20 per hour
Links: More info | Book now
Name: Large meeting room
Short description: A delightful, spacious room with an outlook and access to the small walled garden. Ideal for meetings and small gatherings - it has its own access door and the use of a disabled W/C. We offer a reduced rate for this room when booked together with the main hall.
Capacity: 20 people
Price: £6-12 per hour
Attachments:
We have attached some photos of the hall & some (royalty free) stock images for inspiration.

```html
<!DOCTYPE html>
<html lang="en">
<head>
<meta charset="utf-8">
<title>Fallowmere community hall — Home</title>
<link href="https://fonts.googleapis.com/css2?family=Montserrat:wght@400;500;600;700;800&family=Questrial&display=swap" rel="stylesheet">
<style>
:root{
  --red:#f23a16;
  --red-deep:#c92a0d;
  --ink:#2b2b2b;
  --body:#555;
  --muted:#9a9a9a;
  --dark-card:#333;
  --paper:#fff;
  --mist:#f1f0f0;
}
*{box-sizing:border-box;margin:0;padding:0}
html,body{width:1200px;height:4357px;overflow:hidden}
body{position:relative;background:var(--paper);font-family:"Questrial",sans-serif;color:var(--body)}
.abs{position:absolute}
.heading{font-family:"Montserrat",sans-serif;font-weight:600;color:var(--red);font-size:16px;letter-spacing:.3px;text-transform:uppercase}
.heading::before{content:"";position:absolute;left:0;top:-10px;width:52px;height:2px;background:var(--red)}
.heading.center::before{left:50%;margin-left:-38px;width:76px}
.copy{font-size:12.5px;line-height:22.5px;color:var(--body)}
.btn{display:flex;align-items:center;justify-content:center;border-radius:20px;font-family:"Montserrat",sans-serif;font-size:12px;text-transform:uppercase;text-decoration:none}
.btn.solid{background:var(--red);color:#fff}
.btn.ghost{border:1.5px solid var(--red);color:var(--red);background:#fff}
.topline{left:0;top:0;width:1200px;height:3px;background:var(--red)}
/* header brand */
.brand{display:flex;align-items:center;gap:8px;font-family:"Questrial",sans-serif;font-weight:400;white-space:nowrap}
.brand i{display:block;width:12px;height:12px;background:currentColor}
.brand-top{left:150px;top:22px;font-size:14px;color:var(--red)}
.hero-photo{left:418px;top:0;width:782px;height:452px;border-bottom-left-radius:240px;background:linear-gradient(160deg,#7fa0c6 0%,#b58aa0 30%,#6a3a3a 60%,#2a1512 100%)}
.nav{left:505px;top:30px;display:flex;align-items:center}
.nav a{color:#fff;font-family:"Montserrat",sans-serif;font-size:10px;text-decoration:none;text-transform:uppercase;width:86px;text-align:center}
.nav a.active{color:var(--red)}
.nav a.contact{background:var(--red);border-radius:14px;padding:6px 0;width:92px;margin-left:8px}
.hero-title{left:150px;top:135px;width:320px;font-family:"Montserrat",sans-serif;font-weight:700;font-size:24px;line-height:30px;color:var(--red);text-transform:uppercase;white-space:nowrap}
.hero-copy{left:150px;top:204px;width:270px;font-size:12.5px;line-height:22px;color:var(--ink)}
.hero-btn{left:152px;top:315px;width:186px;height:34px}
/* about */
.about-photo{left:156px;top:511px;width:450px;height:374px;border-radius:70px 0 190px 0;background:linear-gradient(150deg,#3b1a8a,#7b3fd0 45%,#c06ad8 70%,#3a1a6a);box-shadow:0 16px 30px rgba(0,0,0,.18)}
.about-head{left:652px;top:520px}
.about-copy{left:652px;top:563px;width:400px}
/* events */
.events-head{left:150px;top:985px}
.event-date{left:153px;top:1026px;border-left:3px solid var(--red);padding-left:4px;font-family:"Montserrat",sans-serif;color:var(--ink);font-weight:800;line-height:1}
.event-date .d{font-size:32px}
.event-date .m{font-size:16px}
.event-date .y{font-size:13px}
.event-title{left:211px;top:1028px;font-family:"Montserrat",sans-serif;font-size:11.5px;color:var(--red);text-transform:uppercase}
.event-link{left:463px;top:1033px;width:40px;height:1px;background:var(--red)}
.event-copy{left:211px;top:1063px;width:255px}
.event-copy a{color:var(--red);text-decoration:none;text-transform:uppercase}
.slider{left:266px;top:1265px;display:flex;gap:8px;align-items:center}
.dot{width:7px;height:7px;border-radius:50%;background:var(--ink)}
.dot.on{background:var(--red)}
.cal{left:547px;top:961px;width:502px;height:342px;background:#fff;box-shadow:0 6px 26px rgba(0,0,0,.16)}
.cal-year{left:549px;top:958px;font-family:"Montserrat",sans-serif;font-weight:800;font-size:68px;color:#1b1b1b;letter-spacing:-3px;line-height:1}
.cal-photo{left:553px;top:1022px;width:154px;height:188px;background:linear-gradient(180deg,#2d1f3f,#6c4a2c 55%,#3a2b3a)}
.cal-left-title{left:576px;top:1227px;font-family:"Montserrat",sans-serif;font-size:8px;color:var(--red)}
.cal-left-copy{left:576px;top:1243px;width:112px;font-size:5.5px;line-height:8px;color:var(--muted)}
.cal-divider{left:707px;top:961px;width:1px;height:342px;background:#eee}
.cal-month{left:751px;top:985px;font-family:"Montserrat",sans-serif;font-weight:700;font-size:14px;color:var(--red);letter-spacing:1px}
.cal-month span{color:var(--muted);font-weight:400}
.cal-grid{left:751px;top:1025px;width:258px;display:grid;grid-template-columns:repeat(7,1fr);font-family:"Montserrat",sans-serif;font-size:6px;text-align:center}
.cal-grid .wd{background:var(--red);color:#fff;height:11px;line-height:11px}
.cal-grid .c{height:27px;line-height:27px;color:var(--ink)}
.cal-grid .c.out{color:#ccc}
.cal-grid .c.sel{background:var(--red);color:#fff}
.cal-notes{left:751px;top:1225px;font-family:"Montserrat",sans-serif;font-weight:700;font-size:8px;color:var(--red)}
.cal-notes-box{left:751px;top:1238px;width:258px;height:44px;border:1px solid #e6e6e6}
/* rooms */
.rooms-head{left:0;top:1431px;width:1200px;text-align:center}
.card-back{border-radius:3px}
.room-photo{border:2px solid var(--red);border-radius:4px;box-shadow:0 10px 26px rgba(0,0,0,.25)}
.room-name{font-family:"Montserrat",sans-serif;font-weight:600;font-size:15px;color:var(--red);text-transform:uppercase}
.room-copy{font-size:12.5px;line-height:22.5px;color:var(--body)}
.label{font-family:"Montserrat",sans-serif;font-size:12px;color:var(--red);text-transform:uppercase}
.val{font-size:13px;color:var(--ink)}
.val em{font-style:normal;color:var(--red)}
/* gallery */
.gallery-band{left:0;top:2552px;width:1200px;height:1070px;background:var(--mist)}
.gallery-head{left:0;top:2597px;width:1200px;text-align:center}
.gallery-copy{left:150px;top:2628px;width:900px;text-align:center;font-size:12.5px;line-height:22px;color:var(--body)}
.tile{border:2px solid var(--red)}
.feature{left:555px;top:2716px;width:494px;height:347px;background:linear-gradient(160deg,#f04a2c,#e5391b)}
.feature-frame{left:602px;top:2749px;width:402px;height:284px;border:1.5px solid #fff}
.feature-title{left:555px;top:2874px;width:494px;text-align:center;font-family:"Montserrat",sans-serif;font-size:26px;color:#fff;letter-spacing:.5px}
.gallery-btn{left:499px;top:3570px;width:202px;height:29px;border-radius:3px}
/* testimonials */
.testi-head{left:0;top:3693px;width:1200px;text-align:center}
.avatar{border-radius:50%;background:linear-gradient(160deg,#8a8a8a,#3b3b3b)}
.arrow{width:0;height:0;border-top:10px solid transparent;border-bottom:10px solid transparent}
.arrow.l{border-right:14px solid var(--red)}
.arrow.r{border-left:14px solid var(--red)}
.testi-name{left:0;top:3864px;width:1200px;text-align:center;font-family:"Montserrat",sans-serif;font-size:15px;color:var(--red);text-transform:uppercase;letter-spacing:.5px}
.stars{left:0;top:3888px;width:1200px;text-align:center;font-size:13px;color:var(--ink);letter-spacing:1px}
.testi-copy{left:245px;top:3930px;width:710px;text-align:center;font-size:16px;line-height:26.5px;color:var(--body)}
.testi-dots{left:572px;top:4061px;display:flex;gap:6px}
/* footer */
.footer{left:0;top:4135px;width:1200px;height:209px;background:var(--red);border-top-right-radius:150px}
.fnav{left:320px;top:4168px;display:flex;width:560px;justify-content:space-between}
.fnav a{color:#fff;font-family:"Montserrat",sans-serif;font-size:10px;text-decoration:none;text-transform:uppercase}
.frule{left:150px;top:4195px;width:900px;height:1px;background:rgba(255,255,255,.6)}
.brand-foot{left:150px;top:4240px;font-size:15px;color:#fff}
.fcopy{left:394px;top:4223px;width:430px;font-size:10px;line-height:19px;color:#fff}
.social{left:866px;top:4219px;display:grid;grid-template-columns:26px 26px;gap:12px 20px}
.social i{display:block;width:26px;height:26px;border-radius:50%;background:#fff}
.bottombar{left:0;top:4344px;width:1200px;height:13px;background:var(--red-deep);color:#fff;font-size:9.5px;line-height:13px;font-family:"Montserrat",sans-serif}
.bottombar .l{position:absolute;left:150px}
.bottombar .r{position:absolute;right:130px}
</style>
</head>
<body>
<div class="abs hero-photo" role="img" aria-label="Photo of a crowd at a concert with confetti and stage lights"></div>
<div class="abs topline"></div>
<div class="abs brand brand-top"><i></i>Fallowmere community hall</div>
<nav class="abs nav">
  <a class="active" href="#">Home</a><a href="#">Calendar</a><a href="#">Facilities</a><a href="#">Prices</a><a href="#">Photos</a><a href="#">News</a><a class="contact" href="#">Contact</a>
</nav>
<h1 class="abs hero-title">Lorem ipsum dolor<br>sit amet, consectetur</h1>
<p class="abs hero-copy">adipiscing elit. Aenean ante eros, ullamcorp er quis dignissim eget, volutpat interdum lec tus. Sed interdum convallis dui et lobortis. Sed lobortis ex</p>
<a class="abs btn solid hero-btn" href="#">Book now</a>

<div class="abs about-photo" role="img" aria-label="Photo of the hall interior lit in purple with string lights"></div>
<h2 class="abs heading about-head">About Fallowmere community hall</h2>
<div class="abs copy about-copy">
  <p>ultrices a nisl. Cras maximus bibendum eros, non rutrum arcu bibendum nec. Etiam quis orci leo. Class aptent taciti sociosqu ad litora torquent per conubia nostra, per inceptos himenaeos. Pellentesque aliquet scelerisque risus sit amet lobortis In lobortis, tortor et elementum Etiam scelerisque lectus purus, eget ultrices ligula ullamcorper eget. In tempor erat vitae</p>
  <p style="margin-top:22px">molestie ullamcorper. Proin consequat sem nec arcu convallis pretium. Pellentesque habitant morbi tristique senectus et netus et malesuada fames ac turpis egestas. Maecenas euismod, elit quis elementum porttitor, augue odio dapibus arcu, sed bibendum felis diam , pharetra a mollis dictum,</p>
</div>

<h2 class="abs heading events-head">Our upcoming activities &amp; events.</h2>
<div class="abs event-date"><div class="d">26</div><div class="m">JAN</div><div class="y">2021</div></div>
<div class="abs event-title">Dolor, finibus non cursus dapibus,</div>
<div class="abs event-link"></div>
<p class="abs copy event-copy">ultrices a nisl. Cras maximus bibendum eros, non rutrum arcu bibendum nec. Etiam quis orci leo. Class aptent taciti sociosqu ad litora torquent per conubia nostra, per inceptos himenaeos. Pellentesque aliquet scelerisque risus sit amet lobortis In lobortis, tortor et elementum laoreet <a href="#">Read more...</a></p>
<div class="abs slider"><span class="arrow l"></span><span class="dot on"></span><span class="dot"></span><span class="dot"></span><span class="dot"></span><span class="dot"></span><span class="arrow r"></span></div>

<div class="abs cal"></div>
<div class="abs cal-photo" role="img" aria-label="Photo of an event table centrepiece"></div>
<div class="abs cal-year">2021</div>
<div class="abs cal-divider"></div>
<div class="abs cal-left-title">Lorem ipsum</div>
<p class="abs cal-left-copy">Donec vitae lobortis risus, fringilla nibh risus, et mollis turpis lacinia a integer eu neque.</p>
<div class="abs cal-month">JANUARY <span>/ 01</span></div>
<div class="abs cal-grid">
  <div class="wd">S</div><div class="wd">M</div><div class="wd">T</div><div class="wd">W</div><div class="wd">T</div><div class="wd">F</div><div class="wd">S</div>
  <div class="c out">27</div><div class="c out">28</div><div class="c out">29</div><div class="c out">30</div><div class="c out">31</div><div class="c">1</div><div class="c">2</div>
  <div class="c">3</div><div class="c">4</div><div class="c">5</div><div class="c">6</div><div class="c">7</div><div class="c">8</div><div class="c">9</div>
  <div class="c">10</div><div class="c">11</div><div class="c">12</div><div class="c">13</div><div class="c">14</div><div class="c">15</div><div class="c">16</div>
  <div class="c">17</div><div class="c">18</div><div class="c">19</div><div class="c">20</div><div class="c">21</div><div class="c">22</div><div class="c">23</div>
  <div class="c">24</div><div class="c">25</div><div class="c sel">26</div><div class="c">27</div><div class="c">28</div><div class="c">29</div><div class="c">30</div>
  <div class="c">31</div><div class="c out">1</div><div class="c out">2</div><div class="c out">3</div><div class="c out">4</div><div class="c out">5</div><div class="c out">6</div>
</div>
<svg class="abs" style="left:700px;top:1030px" width="130" height="140" viewBox="0 0 130 140"><line x1="2" y1="2" x2="118" y2="134" stroke="#f23a16" stroke-width="1"/></svg>
<div class="abs cal-notes">NOTES</div>
<div class="abs cal-notes-box"></div>

<h2 class="abs heading center rooms-head">Our most popular rooms</h2>
<div class="abs card-back" style="left:140px;top:1540px;width:450px;height:300px;background:var(--red);transform:rotate(-28deg) translate(40px,10px)"></div>
<div class="abs card-back" style="left:150px;top:1560px;width:450px;height:300px;background:var(--dark-card);transform:rotate(18deg)"></div>
<div class="abs room-photo" style="left:150px;top:1559px;width:449px;height:298px;background:linear-gradient(160deg,#6e5aa8,#4c3a68 40%,#3a2f2a 75%,#5a4a40)" role="img" aria-label="Photo of the main hall with guests seated at round tables"></div>
<h3 class="abs room-name" style="left:711px;top:1585px">Main hall</h3>
<p class="abs room-copy" style="left:711px;top:1613px;width:330px">A 127 square metre main hall with entrance lobby, toilets, a well-equipped kitchen and separate storage facilities. Three sets of double doors provide access to a large paved area and the adjacent playing field.</p>
<div class="abs label" style="left:711px;top:1744px">Capacity</div>
<div class="abs val" style="left:711px;top:1766px">180 people</div>
<div class="abs label" style="left:921px;top:1744px">Price</div>
<div class="abs val" style="left:921px;top:1766px"><em>£10-20</em> per hour</div>
<a class="abs btn solid" style="left:711px;top:1799px;width:152px;height:29px" href="#">Book now</a>
<a class="abs btn ghost" style="left:889px;top:1799px;width:152px;height:29px" href="#">More info</a>

<h3 class="abs room-name" style="left:150px;top:2083px">Large meeting room</h3>
<p class="abs room-copy" style="left:150px;top:2109px;width:340px">A delightful, spacious room with an outlook and access to the small walled garden. Ideal for meetings and small gatherings - it has its own access door and the use of a disabled W/C. We offer a reduced rate for this room when booked together with the main hall.</p>
<div class="abs label" style="left:150px;top:2258px">Capacity</div>
<div class="abs val" style="left:150px;top:2280px">20 people</div>
<div class="abs label" style="left:360px;top:2258px">Price</div>
<div class="abs val" style="left:360px;top:2280px"><em>£6-12</em> per hour</div>
<a class="abs btn solid" style="left:150px;top:2320px;width:151px;height:29px" href="#">Book now</a>
<a class="abs btn ghost" style="left:325px;top:2320px;width:152px;height:29px" href="#">More info</a>
<div class="abs card-back" style="left:600px;top:2060px;width:450px;height:300px;background:var(--red);transform:rotate(22deg)"></div>
<div class="abs card-back" style="left:590px;top:2070px;width:450px;height:300px;background:var(--dark-card);transform:rotate(-18deg)"></div>
<div class="abs room-photo" style="left:597px;top:2068px;width:449px;height:298px;background:linear-gradient(170deg,#9fb0c4,#7d6a58 45%,#b08a60 70%,#4e4038)" role="img" aria-label="Photo of a team meeting around a long table with laptops"></div>

<div class="abs gallery-band"></div>
<h2 class="abs heading center gallery-head">Our gallary</h2>
<p class="abs gallery-copy">A delightful, spacious room with an outlook and access to the small walled garden. Ideal for meetings and small gatherings - it has its own access door and the use of a disabled W/C. We offer a reduced rate for this room when booked together with the main hall.</p>
<div class="abs tile" style="left:150px;top:2716px;width:389px;height:281px;background:linear-gradient(180deg,#6a4a7a,#c85a3a 40%,#3a3a7a 70%,#d8d8e0)" role="img" aria-label="Photo of stained glass windows above a set dining table"></div>
<div class="abs tile" style="left:150px;top:3014px;width:389px;height:273px;background:linear-gradient(180deg,#e6dccb,#c0a888 50%,#3a4a7a 80%,#8a6a50)" role="img" aria-label="Photo of the hall laid out with round tables"></div>
<div class="abs feature" role="img" aria-label="Photo of a conference room set for a meeting, red overlay"></div>
<div class="abs feature-frame"></div>
<div class="abs feature-title">QUISQUE ERAT TORTOR</div>
<svg class="abs" style="left:758px;top:3005px" width="46" height="54" viewBox="0 0 46 54"><path d="M14 4a4 4 0 0 1 8 0v20l2-1a4 4 0 0 1 8 1l2-1a4 4 0 0 1 8 2v12c0 9-6 16-14 16h-4c-5 0-8-3-11-7L3 34a4 4 0 0 1 6-5l5 5z" fill="#fff"/></svg>
<div class="abs tile" style="left:555px;top:3082px;width:494px;height:205px;background:linear-gradient(180deg,#e8e2d6,#b8945a 35%,#2a3a8a 65%,#d8d8e0)" role="img" aria-label="Photo of the hall with a stained glass window and tables"></div>
<div class="abs tile" style="left:150px;top:3305px;width:899px;height:224px;background:linear-gradient(160deg,#e4e6e4,#d8b680 40%,#6a5a9a 65%,#2e3238)" role="img" aria-label="Photo of a meeting room with tables and purple chairs"></div>
<a class="abs btn solid gallery-btn" href="#">Show all of them</a>

<h2 class="abs heading center testi-head">Client testimonials</h2>
<span class="abs arrow l" style="left:350px;top:3785px"></span>
<div class="abs avatar" style="left:410px;top:3777px;width:36px;height:36px" role="img" aria-label="Client portrait"></div>
<div class="abs avatar" style="left:487px;top:3770px;width:50px;height:50px" role="img" aria-label="Client portrait"></div>
<div class="abs avatar" style="left:562px;top:3760px;width:72px;height:72px;border:3px solid var(--red)" role="img" aria-label="Portrait of Betty D. Torres"></div>
<div class="abs avatar" style="left:657px;top:3770px;width:50px;height:50px" role="img" aria-label="Client portrait"></div>
<div class="abs avatar" style="left:750px;top:3777px;width:36px;height:36px" role="img" aria-label="Client portrait"></div>
<span class="abs arrow r" style="left:834px;top:3785px"></span>
<div class="abs testi-name">Betty D. Torres</div>
<div class="abs stars">★★★★☆</div>
<p class="abs testi-copy">Donec vitae lobortis risus. Vestibulum fringilla nibh risus, et mollis turpis lacinia a. Integer eu scelerisque neque. Fusce metus quam, sagittis in tincidunt ultricies, efficitur vulputate mi. Vestibulum accumsan lacus eros, quis tincidunt est varius vitae. Ut id ligula id quam tempor auctor in id purus. Nullam ultricies condimentum libero sit amet faucibus.</p>
<div class="abs testi-dots"><span class="dot"></span><span class="dot on"></span><span class="dot"></span><span class="dot"></span><span class="dot"></span></div>

<footer>
  <div class="abs footer"></div>
  <nav class="abs fnav"><a href="#">Home</a><a href="#">Calendar</a><a href="#">Facilities</a><a href="#">Prices</a><a href="#">Photos</a><a href="#">News</a><a href="#">Contact</a></nav>
  <div class="abs frule"></div>
  <div class="abs brand brand-foot"><i></i>Fallowmere community hall</div>
  <p class="abs fcopy">Donec vitae lobortis risus. Vestibulum fringilla nibh risus, et mollis turpis lacinia a. Integer eu scelerisque neque. Fusce metus quam, sagittis auctor in id purus. Nullam ultricies condimentum libero sit amet faucibus.</p>
  <div class="abs social" aria-label="Chatterbook, Quipper and other social links"><i></i><i></i><i></i><i></i></div>
  <div class="abs bottombar"><span class="l">© ALL COPYRIGHTS ARE RESEVED</span><span class="r">LOGIN &nbsp;|&nbsp; REGISTER &nbsp;|&nbsp; PRIVACY POLICY &nbsp;|&nbsp; TERMS &amp; CONDITIONS</span></div>
</footer>
</body>
</html>
```